Re Design of Business Cards

We a Technology & Telecommunications company, we supply computer repairs suppy and services to home and business's, we also a Telecommunications company as well and that we supply Internet, Mobile Voice and Data and Voice Lines to home and business as well we want to get our business cards re designed that stand out but also state what we can do and that we also come to you, there is 4 of us in the business so we all need same business card design but just different names and phone numbers on all.
Ive upload our Logo as well. and current looking business cards.

Our current business cards does not make me excited and or stand out, to dark and does not say what we do, we leave our business cards in letter boxes some times and in receptions of villages for retiress so the reception can hand out, few times now there asked what do you do, so thinking one side is our contact details and other is our services

I think I like to also put our address onto it as well, very simple as its also my home address but it be good to have it on there

48 Tindall Cres - Corvan Heights NSW 2318

We should also have our business rego number which is a ABN

ABN: 92 417 306 845

this way we all covered and we look very Professional

We would like to make some Points, 1st of All we just found out we do not need out ABN on our Business Cards so we can Remove that please

we would like the address for the business to be on cards as well,

On the flip side of the Business Cards we would like to list some of our services as below

High-Speed Internet for Home & Business
Managed IT Services & Support
Network Setup & Optimization
VoIP & Mobile Voice Solutions
Wi-Fi Installation & Troubleshooting
Smart Home & Office Technology
Data Backup & Cybersecurity
Onsite Home and Or Business

```html
<!DOCTYPE html>
<html lang="en">
<head>
<meta charset="utf-8">
<title>Kestrova Business Cards</title>
<link rel="stylesheet" href="https://fonts.googleapis.com/css2?family=Poppins:wght@400;500;600;700&display=swap">
<style>
  :root {
    --stage: #1d1e20;
    --teal: #06363a;
    --teal-deep: #042c30;
    --orange: #f26a24;
    --orange-dark: #d95a1c;
    --green: #12c60f;
    --green-dark: #0a9a0a;
    --white: #ffffff;
  }
  * { box-sizing: border-box; margin: 0; padding: 0; }
  html, body { width: 1200px; height: 1200px; overflow: hidden; }
  body {
    background: var(--stage);
    font-family: "Poppins", sans-serif;
    color: var(--white);
    position: relative;
  }
  .card {
    position: absolute;
    left: 120px;
    width: 960px;
    height: 540px;
    background: var(--teal);
    overflow: hidden;
    box-shadow: 0 12px 30px rgba(0,0,0,.55);
  }
  .card--services { top: 45px; }
  .card--contact { top: 615px; }

  .brand {
    position: absolute;
    display: flex;
    align-items: center;
    gap: 18px;
  }
  .brand__dot {
    border-radius: 50%;
    background: var(--orange);
  }
  .brand__name {
    font-weight: 600;
    color: var(--orange);
    letter-spacing: .14em;
    line-height: 1;
  }
  .card--services .brand { left: 60px; top: 50px; }
  .card--services .brand__dot { width: 64px; height: 64px; }
  .card--services .brand__name { font-size: 46px; }

  .services__heading {
    position: absolute;
    left: 60px; top: 150px;
    font-size: 22px; font-weight: 700;
    color: var(--orange);
    letter-spacing: .02em;
  }
  .services__list {
    position: absolute;
    left: 60px; top: 192px;
    list-style: none;
  }
  .services__item {
    display: flex; align-items: center; gap: 14px;
    font-size: 21px; font-weight: 500;
    line-height: 34px;
  }
  .services__bullet {
    width: 14px; height: 14px; border-radius: 50%;
    background: var(--orange);
    flex: none;
  }
  .services__decor {
    position: absolute; right: 0; top: 0;
    width: 380px; height: 540px;
  }

  .card--contact .brand { left: 60px; top: 55px; }
  .card--contact .brand__dot { width: 90px; height: 90px; }
  .card--contact .brand__name { font-size: 62px; }

  .social {
    position: absolute; right: 90px; top: 150px;
    display: flex; gap: 18px;
  }
  .social__link {
    width: 44px; height: 44px; border-radius: 50%;
    background: var(--green);
  }

  .person { position: absolute; left: 60px; top: 225px; }
  .person__name { font-size: 30px; font-weight: 700; letter-spacing: .02em; line-height: 1.1; }
  .person__role { font-size: 24px; color: var(--orange); line-height: 1.2; }

  .divider {
    position: absolute; left: 60px; right: 90px; top: 310px;
    height: 3px; background: var(--green);
  }

  .contact-list {
    position: absolute; left: 60px; top: 330px;
    list-style: none;
  }
  .contact-list__item {
    display: flex; align-items: center; gap: 14px;
    font-size: 24px; line-height: 40px;
  }
  .contact-list__icon {
    width: 28px; height: 28px; border-radius: 50%;
    background: var(--orange);
    display: flex; align-items: center; justify-content: center;
    flex: none;
  }

  .address {
    position: absolute; right: 90px; top: 340px;
    text-align: right; font-size: 24px; line-height: 1.35;
  }

  .footer-bands { position: absolute; left: 0; bottom: 0; width: 960px; height: 110px; }
  .abn {
    position: absolute; right: 90px; bottom: 28px;
    font-size: 26px; font-weight: 500;
  }
</style>
</head>
<body>

<section class="card card--services" aria-label="Services side">
  <div class="brand">
    <span class="brand__dot"></span>
    <span class="brand__name">KESTROVA</span>
  </div>
  <h2 class="services__heading">OUR SERVICES</h2>
  <ul class="services__list">
    <li class="services__item"><span class="services__bullet"></span>High-Speed Internet for Home &amp; Business</li>
    <li class="services__item"><span class="services__bullet"></span>Managed IT Services &amp; Support</li>
    <li class="services__item"><span class="services__bullet"></span>Network Setup &amp; Optimization</li>
    <li class="services__item"><span class="services__bullet"></span>VoIP &amp; Mobile Voice Solutions</li>
    <li class="services__item"><span class="services__bullet"></span>Wi-Fi Installation &amp; Troubleshooting</li>
    <li class="services__item"><span class="services__bullet"></span>Smart Home &amp; Office Technology</li>
    <li class="services__item"><span class="services__bullet"></span>Data Backup &amp; Cybersecurity</li>
    <li class="services__item"><span class="services__bullet"></span>Onsite Home and Or Business</li>
  </ul>
  <svg class="services__decor" viewBox="0 0 380 540" aria-hidden="true">
    <path d="M150 0 H380 V540 H170 C90 460 70 330 90 230 C105 140 125 60 150 0 Z" fill="var(--orange)"/>
    <path d="M300 0 H380 V540 H310 C270 440 260 300 270 200 C278 110 288 50 300 0 Z" fill="var(--green)"/>
  </svg>
</section>

<section class="card card--contact" aria-label="Contact side">
  <div class="brand">
    <span class="brand__dot"></span>
    <span class="brand__name">KESTROVA</span>
  </div>

  <div class="social" aria-label="Social media">
    <span class="social__link" aria-label="Social profile"></span>
    <span class="social__link" aria-label="Social profile"></span>
  </div>

  <div class="person">
    <p class="person__name">MILO TRENTHAM</p>
    <p class="person__role">Sales Consultant</p>
  </div>

  <div class="divider"></div>

  <ul class="contact-list">
    <li class="contact-list__item">
      <span class="contact-list__icon">
        <svg width="16" height="16" viewBox="0 0 24 24"><path d="M6.6 10.8a15 15 0 0 0 6.6 6.6l2.2-2.2a1 1 0 0 1 1-.25 11.4 11.4 0 0 0 3.6.57 1 1 0 0 1 1 1V20a1 1 0 0 1-1 1A17 17 0 0 1 3 4a1 1 0 0 1 1-1h3.5a1 1 0 0 1 1 1c0 1.25.2 2.45.57 3.57a1 1 0 0 1-.25 1z" fill="var(--white)"/></svg>
      </span>1800 614 372
    </li>
    <li class="contact-list__item">
      <span class="contact-list__icon">
        <svg width="14" height="16" viewBox="0 0 14 20"><rect x="1" y="1" width="12" height="18" rx="2" fill="none" stroke="var(--white)" stroke-width="2"/><circle cx="7" cy="15.5" r="1.2" fill="var(--white)"/></svg>
      </span>0471 583 096
    </li>
    <li class="contact-list__item">
      <span class="contact-list__icon">
        <svg width="16" height="12" viewBox="0 0 20 14"><rect x="1" y="1" width="18" height="12" fill="none" stroke="var(--white)" stroke-width="2"/><path d="M1 1 L10 8 L19 1" fill="none" stroke="var(--white)" stroke-width="2"/></svg>
      </span>milo@kestrova.com.au
    </li>
  </ul>

  <address class="address" style="font-style:normal">
    48 Tindall Cres<br>Corvan Heights NSW 2318
  </address>

  <svg class="footer-bands" viewBox="0 0 960 110" aria-hidden="true">
    <path d="M0 20 L500 80 L500 110 L0 110 Z" fill="var(--green)"/>
    <path d="M470 110 C500 60 530 30 600 30 L960 30 V110 Z" fill="var(--orange)"/>
  </svg>
  <p class="abn">ABN: 92 417 306 845</p>
</section>

</body>
</html>
```